Packaging design for a reclosable bag for our product

We have a logo, and we need to put it on packaging for our product and while we want the look to be simple, we want it to follow good design principles and also contain spaces for other product descriptions.

There will be 5 sizes at launch so I'd like 5 variations, one for each size.

I've included a few mockups of the type of bag that I made but they are all just rough ideas that I had.

I want the brand to look scientific and methodical and even a bit quirky, as in "wow this is a serious product but also a bit unusual."

```html
<!DOCTYPE html>
<html lang="en">
<head>
<meta charset="utf-8">
<title>QV7 Bias Lighting – Extra Large 5m Pouch</title>
<link href="https://fonts.googleapis.com/css2?family=Open+Sans:wght@700&family=Roboto+Condensed:wght@400;700&family=Roboto:wght@400&family=Archivo+Black&display=swap" rel="stylesheet">
<style>
  :root {
    --backdrop: #9a9a9e;
    --pouch: #262626;
    --pouch-edge: #1c1c1c;
    --zip-line: #161616;
    --ink-white: #f4f4f4;
    --ink-grey: #a4a4a4;
    --outline-grey: #8a8a8a;
  }
  * { margin: 0; padding: 0; box-sizing: border-box; }
  html, body {
    width: 1023px;
    height: 1200px;
    overflow: hidden;
    background: var(--backdrop);
  }
  .canvas {
    position: relative;
    width: 1023px;
    height: 1200px;
  }
  .pouch {
    position: absolute;
    left: 180px;
    top: 50px;
    width: 660px;
    height: 1100px;
    background: var(--pouch);
    border: 1px solid var(--pouch-edge);
  }
  .tear-notch {
    position: absolute;
    top: 50px;
    width: 14px;
    height: 14px;
    border-radius: 50%;
    background: var(--backdrop);
  }
  .tear-notch--left { left: -7px; }
  .tear-notch--right { right: -7px; }
  .zip-seal {
    position: absolute;
    left: 46px;
    right: 36px;
    top: 104px;
    height: 6px;
    border-top: 2px solid var(--zip-line);
    border-bottom: 2px solid var(--zip-line);
  }
  .brand-block {
    position: absolute;
    left: 338px;
    top: 355px;
    width: 230px;
    color: var(--ink-white);
  }
  .brand-name {
    font-family: "Open Sans", sans-serif;
    font-weight: 700;
    font-size: 150px;
    line-height: 130px;
    letter-spacing: -6px;
    margin-left: -6px;
  }
  .product-line {
    font-family: "Open Sans", sans-serif;
    font-weight: 700;
    font-size: 29px;
    line-height: 34px;
    margin-top: 12px;
    letter-spacing: -0.3px;
  }
  .spec-lines {
    font-family: "Roboto Condensed", sans-serif;
    font-weight: 400;
    font-size: 21px;
    line-height: 26px;
    margin-top: 18px;
  }
  .spec-lines strong { font-weight: 700; }
  .size-label {
    position: absolute;
    left: 345px;
    top: 652px;
    font-family: "Roboto", sans-serif;
    font-size: 33px;
    letter-spacing: 3px;
    color: var(--ink-grey);
  }
  .size-figure {
    position: absolute;
    left: 160px;
    top: 640px;
    width: 440px;
    height: 300px;
  }
  .size-figure text {
    font-family: "Archivo Black", sans-serif;
    font-size: 340px;
    fill: none;
    stroke: var(--outline-grey);
    stroke-width: 1.4;
  }
</style>
</head>
<body>
<div class="canvas">
  <div class="pouch">
    <span class="tear-notch tear-notch--left"></span>
    <span class="tear-notch tear-notch--right"></span>
    <div class="zip-seal"></div>

    <svg class="size-figure" viewBox="0 0 440 300" aria-hidden="true">
      <text x="0" y="285" textLength="430" lengthAdjust="spacingAndGlyphs">5m</text>
    </svg>

    <div class="brand-block">
      <div class="brand-name">QV7</div>
      <div class="product-line">Bias Lighting</div>
      <div class="spec-lines">
        Simulated <strong>D65 CRI90+</strong><br>
        <strong>6500K</strong> White Bias Lighting
      </div>
    </div>

    <div class="size-label">Extra Large</div>
  </div>
</div>
</body>
</html>
```